Catalogue for Eco friendly products

HI We have 2 brands - logos attached
Verdatotenz
Lumawrap

We would like a catalog of these products :

Size of the catalogue: A4 Size

Verdatote - ( www.verdatote.co.nz)
Cotton bags
Canvas bags
Jute bags
Non woven bags
Mudwiser poop bags

Lumawrap
Degradable bin liners
Compostable bin liners
Recycled bin liners
Paper bags
Customised packaging

All products need to be on A4 page which can be inserted in a folder, the main reason for that to make sales presentation as per the customer requirement. All customers don't need all the products.

We are looking for the designer to make a clean feel where both the logos sit comfortably with each other.

We will need 2 main designs:
1 will be the outside folder design
Inside Catalog for the products with place holders for the photographs and words which can be limited to 10-20 words to ensure that design looks uniform. All products are on our website to provide you with an idea of what we are looking for.

Lumawrap packaging logo is included for your reference to get a feel of the products.
Any other information please let me know.
Thanks

Target Market(s)

B2B- Businesses , purchase manager , event managers, Organic shop owners

Font styles to use
Serif
Sans Serif

Colors
add136
abd037
acd037
cadf82
9bcb3c
f37122

Requirements
Must have
• A Clean design and yet interesting , use of green colour is preferred for the design but complimentary earthy colors are ok
• TEXT in design: Attached for 1 product category : Cotton
Nice to have
• Please see the design inspirations which I like. Please note that these are just to give you an idea of what kind of design we would prefer and is to be used as our guidance to you.

```html
<!DOCTYPE html>
<html lang="en">
<head>
<meta charset="utf-8">
<title>Calico Cotton – Verdatote</title>
<link rel="stylesheet" href="https://fonts.googleapis.com/css2?family=Montserrat:wght@500&family=Raleway:wght@400;600&display=swap">
<style>
  :root {
    --paper: #ffffff;
    --mist: #e6eae3;
    --accent-orange: #f37122;
    --body-grey: #6e6e6e;
    --band-green: #cadf82;
    --brand-green: #9bcb3c;
    --bag-light: #f1ece0;
    --bag-shade: #d9d2c1;
  }
  html, body {
    margin: 0;
    padding: 0;
    overflow: hidden;
  }
  .page {
    position: relative;
    width: 795px;
    height: 1200px;
    overflow: hidden;
    background: linear-gradient(180deg, var(--mist) 0%, #f3f5f1 30%, var(--paper) 55%, var(--paper) 100%);
    font-family: "Raleway", sans-serif;
  }
  .product-photo {
    position: absolute;
    left: 215px;
    top: 38px;
    width: 170px;
    height: 352px;
    border-radius: 4px;
    background: linear-gradient(160deg, var(--bag-light) 0%, var(--bag-shade) 100%);
  }
  .product-title {
    position: absolute;
    top: 538px;
    left: 0;
    width: 100%;
    margin: 0;
    text-align: center;
    font-family: "Montserrat", sans-serif;
    font-weight: 500;
    font-size: 37px;
    letter-spacing: 1px;
    color: var(--accent-orange);
  }
  .product-copy {
    position: absolute;
    top: 610px;
    left: 153px;
    width: 492px;
    margin: 0;
    font-size: 24.5px;
    line-height: 35px;
    text-align: justify;
    letter-spacing: 0.4px;
    color: var(--body-grey);
  }
  .brand-mark {
    position: absolute;
    right: 64px;
    bottom: 90px;
    display: flex;
    align-items: center;
    gap: 8px;
    font-family: "Raleway", sans-serif;
    font-weight: 600;
    font-size: 22px;
    color: var(--brand-green);
  }
  .brand-mark .dot {
    width: 18px;
    height: 18px;
    border-radius: 50%;
    background: var(--brand-green);
  }
  .footer-band {
    position: absolute;
    left: 0;
    bottom: 0;
    width: 100%;
    height: 74px;
    background: var(--band-green);
  }
</style>
</head>
<body>
  <main class="page">
    <div class="product-photo" role="img" aria-label="Product photo: natural calico cotton tote bag with long handles and a printed logo panel"></div>

    <h1 class="product-title">CALICO COTTON</h1>

    <p class="product-copy">Calico is made from unbleached 100% cotton. These bags are an eco- friendly, economically priced packaging which will present your product attractively, display&shy;ing your brand and message to your exact specification. Certified Organic Cotton and Fairgrown Certified products available upon request. For a more heavier “upmar&shy;ket” fabric check out our CANVAS range.</p>

    <div class="brand-mark">
      <span class="dot"></span>
      <span class="brand-name">verdatote</span>
    </div>

    <div class="footer-band"></div>
  </main>
</body>
</html>
```